Truck Wrap - Troxa Plumbing

Needing a Truck design wrap that pops and turns heads. Blue and yellow and the colours of choice.

I would like something very similar to the designs I'm posting below.

Eletric Blue and Yellow for colour scheme and I also like the animated character look of the trucks below.

Target Market(s)

local Population

Industry/Entity Type

Plumbing

Colors
0054AA
0677BA
7BADD7
CADEEF
E8F1F8
FFF300
FFF600
FEFA6F
FFFEC7
FFFEE8

Requirements
Must have
• Poppy colours, animated logo, phone number - 1800 462 518 - 24/7 service
Nice to have
• Something Catchy

```html
<!DOCTYPE html>
<html lang="en">
<head>
<meta charset="utf-8">
<title>Troxa Plumbing – Van Side Wrap</title>
<link rel="stylesheet" href="https://fonts.googleapis.com/css2?family=Alfa+Slab+One&family=Anton&display=swap">
<style>
  :root {
    --stage: #e8ecef;
    --electric-blue: #0054aa;
    --mid-blue: #0677ba;
    --soft-blue: #7badd7;
    --yellow: #fff300;
    --olive-yellow: #c9c81a;
    --pale-yellow: #fefa6f;
    --cream: #fffec7;
    --white: #ffffff;
    --ink: #1d2a3a;
  }
  html, body {
    margin: 0;
    width: 1200px;
    height: 800px;
    overflow: hidden;
    background: var(--stage);
  }
  .wrap-panel {
    position: absolute;
    left: 50px;
    top: 170px;
    width: 1100px;
    height: 460px;
    border-radius: 18px;
    overflow: hidden;
  }
  .wrap-panel svg.wrap-graphics {
    position: absolute;
    inset: 0;
  }
  .mascot-area {
    position: absolute;
    left: 300px;
    top: 30px;
    width: 260px;
    height: 370px;
    border-radius: 120px 120px 24px 24px;
    background: radial-gradient(ellipse at 50% 40%, #f2d64a 0%, #3f7fc4 65%, #2c5f93 100%);
    opacity: 0.9;
  }
  .service-headline {
    position: absolute;
    left: 600px;
    top: 170px;
    transform: rotate(-19deg);
    transform-origin: left bottom;
    white-space: nowrap;
  }
  .service-title {
    font-family: "Alfa Slab One", serif;
    font-size: 64px;
    color: var(--white);
    letter-spacing: 1px;
    line-height: 1;
  }
  .service-hours {
    font-family: "Alfa Slab One", serif;
    font-size: 22px;
    color: var(--white);
    margin-left: 4px;
  }
  .service-phone {
    font-family: "Anton", sans-serif;
    font-size: 30px;
    color: var(--yellow);
    letter-spacing: 2px;
    margin: 4px 0 0 150px;
  }
  .brand-plate {
    position: absolute;
    right: 50px;
    bottom: 80px;
    width: 210px;
    height: 56px;
    background: var(--white);
    display: flex;
    align-items: center;
    gap: 10px;
    padding: 0 12px;
    box-sizing: border-box;
  }
  .brand-dot {
    width: 30px;
    height: 30px;
    border-radius: 50%;
    background: var(--electric-blue);
    flex: none;
  }
  .brand-name {
    font-family: "Anton", sans-serif;
    font-size: 22px;
    color: var(--electric-blue);
    letter-spacing: 1px;
  }
</style>
</head>
<body>
  <section class="wrap-panel">
    <svg class="wrap-graphics" width="1100" height="460" viewBox="0 0 1100 460" aria-hidden="true">
      <defs>
        <linearGradient id="yellowBase" x1="0" y1="0" x2="1" y2="0">
          <stop offset="0" stop-color="#b9bd12"/>
          <stop offset="0.45" stop-color="#e6e55a"/>
          <stop offset="1" stop-color="#cfd02a"/>
        </linearGradient>
        <linearGradient id="blueBand" x1="0" y1="0" x2="1" y2="1">
          <stop offset="0" stop-color="#0677ba"/>
          <stop offset="1" stop-color="#0054aa"/>
        </linearGradient>
      </defs>
      <rect class="base-yellow" width="1100" height="460" fill="url(#yellowBase)"/>
      <polygon class="highlight-yellow" points="480,0 720,0 560,200" fill="#fff300" opacity="0.45"/>
      <polygon class="band-top" points="760,140 1030,0 1100,0 1100,40 860,130" fill="url(#blueBand)"/>
      <polygon class="band-headline" points="640,260 720,140 1100,80 1100,200 820,300" fill="url(#blueBand)"/>
      <polygon class="band-lower" points="420,460 1100,260 1100,460" fill="url(#blueBand)"/>
      <polygon class="band-lower-light" points="600,400 1100,250 1100,280 640,410" fill="#7badd7" opacity="0.5"/>
      <line class="accent-line" x1="560" y1="300" x2="1100" y2="150" stroke="#fff300" stroke-width="3"/>
      <line class="accent-line" x1="420" y1="440" x2="760" y2="350" stroke="#fff300" stroke-width="2"/>
      <rect class="sill-stripe" x="0" y="370" width="1100" height="26" fill="#1f2328" opacity="0.85"/>
    </svg>

    <div class="mascot-area" role="img" aria-label="Cartoon plumber mascot in a yellow hard hat and blue overalls standing beside pipes"></div>

    <div class="service-headline">
      <div><span class="service-title">PLUMBING</span><span class="service-hours">24/7</span></div>
      <div class="service-phone">1800 462 518</div>
    </div>

    <div class="brand-plate">
      <span class="brand-dot"></span>
      <span class="brand-name">TROXA PLUMBING</span>
    </div>
  </section>
</body>
</html>
```